I need a flyer made , the flyer can be one page or two pages or three pages . I will be posting this on Instagram and social media platforms. I am a luxury home builder , I am looking to hire a construction project manager . Below are some examples and ideas what can be on the flyer

We’re looking for a construction project manager who’s passionate about building luxury homes at the highest standards
We’re hiring construction project manager
* Experience 5+ years in residential project management with a strong portfolio of completed homes.
* location : Bergen County NJ
* excellent leadership skills, leads teams with confidence and clarity
* communicates seamlessly with architects , engineers, designers and clients
*knows how to manage budgets and timelines without compromising quality
*solves problems with a positive solution first mindset
* pays attention to every detail because in luxury the small things are the big things

Apply now , link in bio or DM to connect.

My logo is attached, my web site www.ridgelanebuilders.com
My style is modern but still warm and inviting. I like a clean classy look .
Updates

Please don’t add any images of chairs or people to the flyer , I do not want people on my flyer. Do not add standard images of offices and houses , we are luxury builders , we build homes over 2 million dollars. Keep a classy , simple modern look . High end .

You can add a white hard hat with my logo on it for a image , this is a suggestion does not have to be on my flyer ,

```html
<!DOCTYPE html>
<html lang="en">
<head>
<meta charset="utf-8">
<title>Ridgelane Builders – We're Hiring</title>
<link href="https://fonts.googleapis.com/css2?family=Poppins:wght@200;300;400;500;700;800&display=swap" rel="stylesheet">
<style>
  :root {
    --stage: #cdd2da;
    --paper: #f0f2f1;
    --ink: #111111;
    --white: #ffffff;
    --muted: #6f7378;
    --sky-top: #1c2438;
    --sky-mid: #3d3f5c;
    --dusk-pink: #c98a9a;
    --dusk-gold: #e0b27a;
    --lawn: #1f3a1c;
    --interior-warm: #c9a784;
    --interior-cool: #b9c4cc;
  }
  * { box-sizing: border-box; margin: 0; padding: 0; }
  html, body {
    width: 1200px; height: 655px; overflow: hidden;
    background: var(--stage);
    font-family: "Poppins", sans-serif;
  }
  .canvas { position: relative; width: 1200px; height: 655px; }
  .card {
    position: absolute; top: 85px; width: 489px; height: 489px;
    overflow: hidden; box-shadow: 0 6px 18px rgba(40,50,70,.18);
  }
  .card--cover { left: 95px; background: var(--paper); }
  .card--details { left: 596px; background: var(--paper); }

  /* Cover card */
  .cover-photo {
    position: absolute; left: 0; top: 0; width: 489px; height: 447px;
    background: linear-gradient(180deg, var(--sky-top) 0%, var(--sky-mid) 28%, var(--dusk-pink) 42%, var(--dusk-gold) 50%, #d9d3c8 62%, #8a8376 76%, var(--lawn) 84%, #14290f 100%);
  }
  .brand-plate {
    position: absolute; left: 322px; top: 12px; width: 167px; height: 49px;
    background: var(--ink);
    display: flex; align-items: center; justify-content: center;
  }
  .brand-name {
    font-family: "Poppins", sans-serif; font-weight: 300;
    letter-spacing: .06em; text-transform: uppercase;
  }
  .brand-plate .brand-name { color: var(--white); font-size: 13px; }
  .headline-top {
    position: absolute; left: 148px; top: 82px;
    font-weight: 200; font-size: 64px; line-height: 1; color: var(--white);
    letter-spacing: -1px;
  }
  .headline-main {
    position: absolute; left: 94px; top: 304px;
    font-weight: 800; font-size: 88px; line-height: 1; color: var(--white);
    letter-spacing: -3px;
  }
  .site-url {
    position: absolute; left: 0; width: 100%; text-align: center;
    font-weight: 300; font-size: 14px; letter-spacing: .22em; color: var(--muted);
  }
  .card--cover .site-url { top: 456px; }

  /* Details card */
  .details-brand {
    position: absolute; left: 0; top: 24px; width: 100%; text-align: center;
  }
  .details-brand .brand-name { color: var(--ink); font-size: 22px; }
  .intro {
    position: absolute; left: 18px; top: 87px; width: 455px;
    font-size: 13.6px; line-height: 1.14; font-weight: 400; color: var(--ink);
  }
  .role-band {
    position: absolute; left: 0; top: 132px; width: 489px; height: 23px;
    background: linear-gradient(90deg, var(--ink) 0%, var(--ink) 62%, rgba(17,17,17,.55) 82%, rgba(17,17,17,0) 100%);
    color: var(--white); font-size: 14.2px; font-weight: 400;
    line-height: 23px; padding-left: 18px; letter-spacing: .01em;
  }
  .requirements { position: absolute; left: 0; top: 174px; list-style: none; }
  .requirements li {
    display: flex; align-items: center; height: 19.5px;
    font-size: 8.6px; font-weight: 300; color: var(--ink);
  }
  .requirements svg { width: 28px; height: 9px; margin-right: 4px; flex: none; }
  .interior-visual {
    position: absolute; left: 210px; top: 292px; width: 279px; height: 197px;
    background: radial-gradient(ellipse at 75% 75%, var(--interior-warm) 0%, rgba(201,167,132,.6) 30%, transparent 65%),
                linear-gradient(200deg, var(--interior-cool) 0%, rgba(185,196,204,.5) 40%, transparent 75%);
    -webkit-mask-image: linear-gradient(90deg, transparent 0%, #000 40%);
            mask-image: linear-gradient(90deg, transparent 0%, #000 40%);
  }
  .apply-cta {
    position: absolute; left: 0; top: 351px; width: 231px; height: 36px;
  }
  .apply-cta svg { position: absolute; inset: 0; }
  .apply-cta p {
    position: relative; padding: 6px 0 0 19px; color: var(--white); line-height: 1.05;
  }
  .apply-cta strong { display: block; font-size: 11.5px; font-weight: 700; }
  .apply-cta span { display: block; font-size: 10px; font-weight: 400; }
  .card--details .site-url { top: 456px; }
</style>
</head>
<body>
<main class="canvas">
  <section class="card card--cover">
    <div class="cover-photo" role="img" aria-label="Modern luxury two-storey home lit from inside at dusk, with pool and lawn"></div>
    <div class="brand-plate"><span class="brand-name">Ridgelane Builders</span></div>
    <h1 class="headline-top">WE’RE</h1>
    <p class="headline-main">HIRING</p>
    <p class="site-url">www.ridgelanebuilders.com</p>
  </section>

  <section class="card card--details">
    <div class="details-brand"><span class="brand-name">Ridgelane Builders</span></div>
    <p class="intro">We’re looking for a construction project manager who’s passionate about building luxury homes at the highest standards</p>
    <h2 class="role-band">WE’RE HIRING CONSTRUCTION PROJECT MANAGER</h2>
    <ul class="requirements">
      <li><svg viewBox="0 0 28 9"><polygon points="0,0 12,0 10,9 0,9" fill="#111"/><polygon points="14,0 16,0 14,9 12,9" fill="#111"/><polygon points="18,0 20,0 18,9 16,9" fill="#111"/><polygon points="22,0 24,0 22,9 20,9" fill="#111"/><polygon points="26,0 28,0 26,9 24,9" fill="#111"/></svg>Experience 5+ years in residential project management with a strong portfolio of completed homes</li>
      <li><svg viewBox="0 0 28 9"><polygon points="0,0 12,0 10,9 0,9" fill="#111"/><polygon points="14,0 16,0 14,9 12,9" fill="#111"/><polygon points="18,0 20,0 18,9 16,9" fill="#111"/><polygon points="22,0 24,0 22,9 20,9" fill="#111"/><polygon points="26,0 28,0 26,9 24,9" fill="#111"/></svg>Location : Bergen County NJ</li>
      <li><svg viewBox="0 0 28 9"><polygon points="0,0 12,0 10,9 0,9" fill="#111"/><polygon points="14,0 16,0 14,9 12,9" fill="#111"/><polygon points="18,0 20,0 18,9 16,9" fill="#111"/><polygon points="22,0 24,0 22,9 20,9" fill="#111"/><polygon points="26,0 28,0 26,9 24,9" fill="#111"/></svg>Excellent leadership skills, leads teams with confidence and clarity</li>
      <li><svg viewBox="0 0 28 9"><polygon points="0,0 12,0 10,9 0,9" fill="#111"/><polygon points="14,0 16,0 14,9 12,9" fill="#111"/><polygon points="18,0 20,0 18,9 16,9" fill="#111"/><polygon points="22,0 24,0 22,9 20,9" fill="#111"/><polygon points="26,0 28,0 26,9 24,9" fill="#111"/></svg>Communicates seamlessly with architects, engineers, designers and clients</li>
      <li><svg viewBox="0 0 28 9"><polygon points="0,0 12,0 10,9 0,9" fill="#111"/><polygon points="14,0 16,0 14,9 12,9" fill="#111"/><polygon points="18,0 20,0 18,9 16,9" fill="#111"/><polygon points="22,0 24,0 22,9 20,9" fill="#111"/><polygon points="26,0 28,0 26,9 24,9" fill="#111"/></svg>Knows how to manage budgets and timelines without compromising quality</li>
      <li><svg viewBox="0 0 28 9"><polygon points="0,0 12,0 10,9 0,9" fill="#111"/><polygon points="14,0 16,0 14,9 12,9" fill="#111"/><polygon points="18,0 20,0 18,9 16,9" fill="#111"/><polygon points="22,0 24,0 22,9 20,9" fill="#111"/><polygon points="26,0 28,0 26,9 24,9" fill="#111"/></svg>Solves problems with a positive solution first mindset</li>
      <li><svg viewBox="0 0 28 9"><polygon points="0,0 12,0 10,9 0,9" fill="#111"/><polygon points="14,0 16,0 14,9 12,9" fill="#111"/><polygon points="18,0 20,0 18,9 16,9" fill="#111"/><polygon points="22,0 24,0 22,9 20,9" fill="#111"/><polygon points="26,0 28,0 26,9 24,9" fill="#111"/></svg>Pays attention to every detail because in luxury the small things are the big things</li>
    </ul>
    <div class="interior-visual" role="img" aria-label="Architectural sketch blending into a finished penthouse living room with city view"></div>
    <div class="apply-cta">
      <svg viewBox="0 0 231 36" preserveAspectRatio="none"><polygon points="0,0 195,0 231,36 0,36" fill="#111"/></svg>
      <p><strong>APPLY NOW,</strong><span>LINK IN BIO OR DM TO CONNECT</span></p>
    </div>
    <p class="site-url">www.ridgelanebuilders.com</p>
  </section>
</main>
</body>
</html>
```